Website Design for a New Business Sharing Application

Purpose: Website for a new product – a sharing application called "Plyqo.io"

Product concept: Easy sharing of business information. The application has different sections: tasks, calendars, documents, contacts, notes and links. The key feature of the application is that you can drag and drop information from different sections into a "share." A share is a page which lists all the types of information that you drag into it. You can add people to this "share."

Note: The application itself is not part of this project, just the website.

Website details: The site, in addition to being informational, will actually be the first point of entry for visitors into the application itself. Because of that, we would like the website design to reflect the look of the application, to create a smooth and seamless experience for the user moving from the website into the application (tough the website does not need to look *exactly* like the application). Included Product Tour screenshots show you the look of the application.

Website pages to be created: 4 pages
We are flexible in terms of the exact structure and placement of elements. You may change that any way you like. The pages are as follows:

Home page
Product Tour page
Press page
Blog page

Specific description of pages are provided in project files we will upload. We will also upload the logo, home page layout we have in mind, and other supporting files.

NOTE: Please submit first the design of the home page. Based on this design we will ask selected designers to submit designs for the other pages.

Target Market(s)

Business people who want to share work related files with their colleagues

Industry/Entity Type

Business

Requirements
Must have
• All the required features are listed in the description of the website and specific pages that we will upload.

```html
<!DOCTYPE html>
<html lang="en">
<head>
<meta charset="utf-8">
<title>Plyqo.io — Share NOW</title>
<link rel="stylesheet" href="https://fonts.googleapis.com/css2?family=Arimo:wght@400;700&family=Open+Sans:ital,wght@0,400;0,600;0,700;1,700;1,800&display=swap">
<style>
  :root {
    --blue: #1b75bb;
    --blue-light: #3f9ee6;
    --orange: #e0670b;
    --orange-bright: #f08a1c;
    --text-dark: #1e1e1e;
    --text-muted: #8a8a8a;
    --header-grey: #e4e4e4;
    --band-grey: #d6d6d6;
    --footer-grey: #efefef;
    --line: #dcdcdc;
    --white: #ffffff;
  }
  * { box-sizing: border-box; margin: 0; padding: 0; }
  html, body { width: 1200px; height: 838px; overflow: hidden; }
  body {
    position: relative;
    background: var(--white);
    font-family: "Arimo", Arial, sans-serif;
    color: var(--text-dark);
  }

  /* Header */
  .site-header {
    position: absolute; left: 0; top: 0; width: 1200px; height: 88px;
    background: linear-gradient(#f0f0f0, var(--header-grey));
  }
  .brand {
    position: absolute; left: 54px; top: 26px;
    display: flex; align-items: center; gap: 10px;
    font-family: "Open Sans", sans-serif; font-weight: 600; font-size: 27px;
    color: var(--blue);
  }
  .brand-dot { width: 24px; height: 24px; border-radius: 50%; background: var(--orange); }
  .account-link {
    position: absolute; right: 59px; top: 31px;
    font-size: 15px; color: var(--text-dark); text-decoration: none;
  }

  /* Hero */
  .hero {
    position: absolute; left: 0; top: 88px; width: 1200px; height: 405px;
    background: linear-gradient(#ffffff 0%, #ffffff 45%, var(--band-grey) 100%);
  }
  .hero-title-box {
    position: absolute; left: 376px; top: 18px; width: 381px; height: 83px;
    background: linear-gradient(#ffffff, #eeeeee);
    box-shadow: 0 1px 3px rgba(0,0,0,.08);
    display: flex; align-items: center; justify-content: center;
  }
  .hero-title {
    font-family: "Open Sans", sans-serif; font-style: italic; font-weight: 700;
    font-size: 52px; letter-spacing: 0.5px;
    color: var(--orange);
  }
  .tagline {
    position: absolute; left: 0; width: 1200px; top: 118px;
    text-align: center; font-size: 19px;
  }
  .content-types {
    position: absolute; left: 327px; top: 150px; width: 536px; height: 38px;
    display: flex; list-style: none;
    background: linear-gradient(#fbfbfb, #ececec);
    border-radius: 2px;
  }
  .content-types li {
    flex: 1 1 auto; text-align: center; line-height: 38px;
    font-size: 13.5px; color: #45586b;
    border-right: 1px solid #c9c9c9;
  }
  .content-types li:last-child { border-right: none; }

  .drop-zone { position: absolute; left: 0; top: 0; }
  .drop-label {
    position: absolute; left: 208px; top: 246px; width: 420px;
    font-family: "Open Sans", sans-serif; font-style: italic; font-weight: 800;
    font-size: 24px; line-height: 29px; color: var(--white);
    letter-spacing: -0.5px;
    text-shadow: 2px 2px 1px rgba(0,0,0,.35);
  }
  .drop-label .first-line { display: block; padding-left: 26px; }
  .or-label {
    position: absolute; left: 620px; top: 265px;
    font-family: "Open Sans", sans-serif; font-style: italic; font-weight: 800;
    font-size: 46px; color: #111;
  }
  .email-input {
    position: absolute; left: 735px; top: 265px; width: 256px; height: 52px;
    background: #f4f4f4; border: none; border-radius: 3px;
    padding-left: 15px; font-family: "Arimo", sans-serif; font-size: 13px; color: #555;
  }
  .start-button {
    position: absolute; left: 759px; top: 332px; width: 210px; height: 47px;
    border: none; border-radius: 3px;
    background: linear-gradient(var(--orange-bright), #d55c08);
    color: var(--white); font-family: "Open Sans", sans-serif; font-weight: 700; font-size: 19px;
    box-shadow: 0 2px 2px rgba(0,0,0,.2);
  }

  /* Intro */
  .intro { position: absolute; left: 0; top: 493px; width: 1200px; height: 242px; background: #fbfbfb; }
  .intro-divider { position: absolute; left: 603px; top: 0; width: 1px; height: 242px; background: var(--line); }
  .intro-question {
    position: absolute; left: 363px; top: 107px;
    font-size: 33px; font-weight: 400; color: var(--blue);
  }
  .video-art {
    position: absolute; left: 672px; top: 83px; width: 94px; height: 89px;
    background: linear-gradient(135deg, #e8e8f4, #9aa0c8); border-radius: 6px;
  }
  .video-link {
    position: absolute; left: 781px; top: 125px; font-size: 19px; color: #3a2a1c;
  }

  /* Footer */
  .site-footer { position: absolute; left: 0; top: 735px; width: 1200px; height: 90px; background: var(--footer-grey); }
  .footer-nav { position: absolute; left: 51px; top: 37px; list-style: none; }
  .footer-nav li { position: absolute; white-space: nowrap; font-size: 12px; color: var(--text-muted); }
  .footer-nav li.is-highlight { color: var(--orange); }
  .social-links { position: absolute; left: 1020px; top: 32px; display: flex; gap: 10px; }
  .social-square { width: 35px; height: 35px; border-radius: 4px; background: linear-gradient(#8c8c8c, #5d5d5d); }
</style>
</head>
<body>
  <header class="site-header">
    <div class="brand"><span class="brand-dot"></span>Plyqo.io</div>
    <a class="account-link" href="#">Access your shares</a>
  </header>

  <section class="hero">
    <div class="hero-title-box"><h1 class="hero-title">Share NOW</h1></div>
    <p class="tagline">Drag information,add people,BOOM!</p>
    <ul class="content-types">
      <li>Files</li><li>Pictures</li><li>Tasks</li><li>To-dos</li><li>Calendars</li><li>Notes</li><li>Links</li>
    </ul>

    <svg class="drop-zone" width="1200" height="405" viewBox="0 0 1200 405" aria-hidden="true">
      <polygon points="63,395 275,227 673,233 485,395" fill="var(--blue-light)"/>
      <polygon points="57,386 269,221 667,227 479,386" fill="var(--blue)"/>
      <polygon points="633,392 744,218 976,214 1083,393" fill="var(--orange)"/>
      <g fill="#333" transform="translate(3,3)">
        <polygon points="430,290 442,290 434,330 422,330"/>
        <polygon points="412,304 456,304 453,315 409,315"/>
      </g>
      <g fill="#fff">
        <polygon points="430,290 442,290 434,330 422,330"/>
        <polygon points="412,304 456,304 453,315 409,315"/>
      </g>
    </svg>
    <p class="drop-label"><span class="first-line">DARG FILES HERE TO SHARE</span>IMMEDIATELY</p>
    <span class="or-label">or</span>
    <input class="email-input" type="email" placeholder="Enter business email">
    <button class="start-button" type="button">Start Sharing</button>
  </section>

  <section class="intro">
    <div class="intro-divider"></div>
    <h2 class="intro-question">What is it?</h2>
    <div class="video-art" role="img" aria-label="Film strip and pages icon for the product video"></div>
    <span class="video-link">watch video</span>
  </section>

  <footer class="site-footer">
    <ul class="footer-nav">
      <li style="left:0">Home</li>
      <li style="left:78px">About us</li>
      <li style="left:177px">Free for unlimited users</li>
      <li style="left:351px">Terms of use</li>
      <li class="is-highlight" style="left:474px">Jobs</li>
      <li style="left:544px">Sign up</li>
      <li style="left:628px">Blog</li>
      <li style="left:689px">Press</li>
      <li style="left:752px">Contact us</li>
    </ul>
    <div class="social-links">
      <span class="social-square" role="img" aria-label="Social network link"></span>
      <span class="social-square" role="img" aria-label="Social network link"></span>
      <span class="social-square" role="img" aria-label="Social network link"></span>
    </div>
  </footer>
</body>
</html>
```